DL size flyer design for renovations and extensions construction company

We are looking for a flyer design for a construction company specialising in renovations, extensions, and minor building works. The aim is for anyone needing any home construction works to pick up the phone and call us. The flyers will be delivered primarily to letterboxes of homes. We want the flyers to stick out from all the other things people get in the mail by any means possible.

Target Market(s)

The audience we target is residential home owners and are looking to deliver these letters to home letterboxes.

Industry/Entity Type

Residential Construction

Font styles to use
Sans Serif

Colors
000000
ffffff

Requirements
Must have
• 1 - Places for 4 photos with descriptions reading: (1) Bathroom Renovations (4) Kitchen Renovations (3) Home Extensions (4) Outdoor works and landscaping. This may be on the reverse side of the DL flyer.
• 2 - Fonts to be used are (1) Brandon Grotesque (All caps) for main heading, (2) Montserrat SemiBold (All caps) for Headings, (3) Lato for text.
• 3 - Copy of the finished document in PDF and indesign formats.
• 4 - Placeholders for copy (look at the plinvaroq.com website for now)
Nice to have
• A modern looking design.
Should not have
• Not all photos attached are necessarily required. Up to you to use your creativity to decide on the best combination.

```html
<!DOCTYPE html>
<html lang="en">
<head>
<meta charset="utf-8">
<title>Plinvaroq – Build, Renovate, Extend</title>
<link rel="stylesheet" href="https://fonts.googleapis.com/css2?family=Montserrat:wght@600;700;800&display=swap">
<style>
  :root {
    --black: #0b0b0b;
    --white: #ffffff;
    --green: #1a9b5f;
    --photo-dark: #5b6268;
    --photo-mid: #9aa3a6;
    --photo-green: #5d7a3c;
  }
  html, body {
    margin: 0;
    padding: 0;
    width: 1200px;
    height: 2542px;
    overflow: hidden;
    background: var(--white);
  }
  .flyer {
    position: relative;
    width: 1200px;
    height: 2542px;
    overflow: hidden;
    font-family: "Montserrat", Arial, sans-serif;
    background: var(--white);
  }
  .flyer-shapes {
    position: absolute;
    inset: 0;
    width: 1200px;
    height: 2542px;
  }
  .brand-name {
    position: absolute;
    left: 62px;
    top: 66px;
    margin: 0;
    font-weight: 800;
    font-size: 78px;
    letter-spacing: 4px;
    color: var(--black);
    line-height: 1;
  }
  .headline {
    position: absolute;
    left: 0;
    width: 1200px;
    top: 1810px;
    margin: 0;
    text-align: center;
    color: var(--white);
    font-weight: 700;
    text-transform: uppercase;
    line-height: 1;
  }
  .headline-line { display: block; font-size: 68px; margin-bottom: 14px; }
  .headline-accent { display: block; font-size: 104px; font-weight: 800; color: var(--green); margin-bottom: 6px; }
  .headline-small { font-size: 56px; }
  .headline-strong { font-size: 96px; font-weight: 800; }
  .services {
    position: absolute;
    left: 0;
    width: 1200px;
    top: 2228px;
    margin: 0;
    text-align: center;
    color: var(--white);
    font-weight: 600;
    font-size: 40px;
    letter-spacing: 2px;
  }
  .website {
    position: absolute;
    left: 0;
    width: 1200px;
    top: 2448px;
    margin: 0;
    text-align: center;
    color: var(--white);
    font-weight: 600;
    font-size: 46px;
  }
</style>
</head>
<body>
<main class="flyer">
  <svg class="flyer-shapes" viewBox="0 0 472 1000" preserveAspectRatio="none" xmlns="http://www.w3.org/2000/svg">
    <defs>
      <linearGradient id="photoTone" x1="0" y1="0" x2="0" y2="1">
        <stop offset="0" stop-color="#b9c2c8"/>
        <stop offset="0.35" stop-color="var(--photo-mid)"/>
        <stop offset="0.65" stop-color="var(--photo-dark)"/>
        <stop offset="1" stop-color="var(--photo-green)"/>
      </linearGradient>
    </defs>
    <rect x="0" y="95" width="472" height="565" fill="url(#photoTone)" role="img" aria-label="Photo of a modern rear house extension with large glass doors, skylight roof and a terraced garden"/>
    <!-- header accents -->
    <polygon points="378,0 472,0 472,88 310,88" fill="var(--green)"/>
    <polygon points="212,96 472,96 472,117 238,117" fill="var(--black)"/>
    <polygon points="244,121 472,121 472,125 247,125" fill="var(--white)"/>
    <!-- lower left angles -->
    <polygon points="0,540 260,660 0,660" fill="var(--white)"/>
    <polygon points="0,553 232,660 204,660 0,566" fill="var(--black)"/>
    <polygon points="0,578 180,660 0,660" fill="var(--green)"/>
    <!-- right side edge -->
    <polygon points="472,560 472,660 300,660" fill="var(--white)"/>
    <polygon points="472,574 472,660 330,660" fill="var(--black)"/>
    <!-- main dark panel -->
    <rect x="0" y="658" width="472" height="300" fill="var(--black)"/>
    <polygon points="0,658 165,658 0,760" fill="var(--green)"/>
    <polygon points="0,650 178,650 172,662 0,662" fill="var(--white)"/>
    <polygon points="472,850 472,958 330,958" fill="var(--white)"/>
    <polygon points="472,866 472,958 360,958" fill="var(--green)"/>
    <!-- footer band -->
    <rect x="0" y="955" width="472" height="45" fill="var(--green)"/>
  </svg>

  <p class="brand-name">PLINVAROQ</p>

  <h1 class="headline">
    <span class="headline-line">Looking</span>
    <span class="headline-line">to make your</span>
    <span class="headline-accent">Home Bigger</span>
    <span><span class="headline-small">or</span> <span class="headline-strong">Better</span></span>
  </h1>

  <p class="services">BUILD • RENOVATE • EXTEND</p>

  <p class="website">www.plinvaroq.com</p>
</main>
</body>
</html>
```